New Real Estate Office in Shell Lake opening Spring 2016

We are a real estate company called 'Pinecove.net'. We are opening a new office in Shell Lake, WI in Spring 2016. We want to announce that on one side of the post card and on the other list 2 pending sales on Shell Lake as well as 3 previous sales. Also mention "Since 2014: Over $20 million in sales; 82 transaction sides; Featured on RVMN's "Harborview Treasure Quest'. Pinecove.net is the #1 most visited lake property website in the midwest. IMG 1991: 827 W. Birch Road: Pending IMG: 2719: N. Fern Rd, Vacant Lot: Pending IMG 4047: SOLD: $490K. IMG 2441: SOLD $505K IMG: Unnamed: SOLD $425K

Target Market(s)

Buyers/Sellers of property in NW WI

Industry/Entity Type

Real Estate Agent

Font styles to use
Serif
Sans Serif

Requirements
Must have
• All uploaded images. My phone #" 555-302-8847
• Words: Realtor/ Broker Associate

```html
<!DOCTYPE html>
<html lang="en">
<head>
<meta charset="utf-8">
<title>Pinecove.net – Lake Property Postcard</title>
<link href="https://fonts.googleapis.com/css2?family=Source+Sans+3:wght@400;600;700&display=swap" rel="stylesheet">
<style>
  :root {
    --blue: #76a0ef;
    --red: #ee1111;
    --ink: #000000;
    --paper: #ffffff;
  }
  * { box-sizing: border-box; margin: 0; padding: 0; }
  html, body { width: 1200px; height: 776px; overflow: hidden; background: var(--paper); }
  body { font-family: "Source Sans 3", "Myriad Pro", sans-serif; position: relative; }

  .headline {
    position: absolute; left: 42px; top: 28px; white-space: nowrap;
    color: var(--blue); font-weight: 700; font-size: 27.5px; line-height: 32.5px;
  }

  .listing-photo {
    position: absolute; width: 138px; height: 138px; border-radius: 50%;
    border: 7px solid var(--red); overflow: hidden; background: var(--paper);
  }
  .listing-photo .fill { width: 100%; height: 100%; }
  .photo-lodge { background: linear-gradient(180deg, #8fb7a0 0%, #6a7d55 40%, #8a5a35 65%, #5ec040 100%); }
  .photo-cabin { background: linear-gradient(180deg, #5d7a44 0%, #9a5a35 45%, #b06a3c 70%, #cdbf9f 100%); }
  .photo-chalet { background: linear-gradient(180deg, #4f7d3a 0%, #8a4a30 45%, #7a4630 70%, #79a04a 100%); }
  .photo-deckhouse { background: linear-gradient(180deg, #c8d6e4 0%, #8a6a4a 40%, #6e5240 65%, #9a8470 100%); }
  .photo-lot { background: linear-gradient(180deg, #9fb6d6 0%, #e3e8ee 40%, #6a7a88 52%, #4b6a2c 62%, #3a5420 100%); }
  .mystery { display: flex; align-items: center; justify-content: center; }
  .mystery span { color: var(--red); font-weight: 700; font-size: 64px; line-height: 1; margin-top: -4px; }

  .tag { position: absolute; color: var(--blue); font-size: 22px; line-height: 28px; white-space: nowrap; }
  .tag .status { color: var(--red); font-weight: 700; font-size: 26px; }
  .sold { position: absolute; color: var(--red); font-size: 26px; line-height: 32px; white-space: nowrap; }
  .sold strong { font-weight: 700; }

  .postage {
    position: absolute; left: 1006px; top: 27px; width: 157px; height: 157px;
    border: 4px solid var(--ink); display: flex; align-items: center; justify-content: center;
    text-align: center; font-size: 22px; line-height: 27px; color: var(--ink);
  }

  .brand-mark {
    position: absolute; left: 1060px; top: 242px; width: 112px; height: 90px;
    display: flex; flex-direction: column; align-items: center; gap: 4px;
  }
  .brand-mark .dot { width: 52px; height: 52px; border-radius: 50%; background: #3f9b45; }
  .brand-mark .name { color: var(--blue); font-weight: 700; font-size: 17px; }

  .address-box {
    position: absolute; left: 35px; top: 354px; width: 733px; height: 299px;
    border: 4px solid var(--ink); border-radius: 3px;
  }

  .announcement {
    position: absolute; left: 800px; top: 372px; width: 370px;
    color: var(--blue); font-size: 22px; line-height: 28px;
  }
  .announcement .title { color: var(--red); font-weight: 700; font-size: 26px; line-height: 32px; margin-bottom: 8px; }
  .announcement .feature { margin-top: 14px; font-weight: 700; }

  .agent-photo {
    position: absolute; left: 23px; top: 677px; width: 78px; height: 75px;
    background: linear-gradient(180deg, #e8dcd2 0%, #d6a88a 45%, #3b5fa8 75%, #2f4f94 100%);
  }
  .agent-name {
    position: absolute; left: 104px; top: 682px; color: var(--blue);
    font-weight: 700; font-size: 22px; white-space: nowrap;
  }
  .agent-phone {
    position: absolute; left: 108px; top: 710px; color: var(--blue); font-size: 23px;
  }
</style>
</head>
<body>
  <p class="headline">Since 2014, over $20 million in sales<br>and 82 transaction sides have made<br>Pinecove.net the #1 most visited<br>lake property website in the Midwest</p>

  <div class="listing-photo" style="left:527px; top:35px;"><div class="fill photo-lodge" role="img" aria-label="Log lake home with green roof and lawn"></div></div>
  <p class="sold" style="left:677px; top:72px;"><strong>SOLD:</strong><br>$505k</p>

  <div class="listing-photo" style="left:779px; top:36px;"><div class="fill photo-cabin" role="img" aria-label="Cedar cabin with wraparound deck among pines"></div></div>
  <p class="sold" style="left:926px; top:71px;"><strong>SOLD:</strong><br>$425k</p>

  <div class="postage">Postage<br>Here</div>

  <div class="listing-photo" style="left:29px; top:194px;"><div class="fill photo-chalet" role="img" aria-label="Chalet-style lake home with deck under trees"></div></div>
  <p class="tag" style="left:176px; top:197px; line-height:29px;">827 W.<br>Birch<br>Road:<br><span class="status">Pending</span></p>

  <div class="listing-photo" style="left:282px; top:195px;"><div class="fill photo-deckhouse" role="img" aria-label="Two-story lake house with balcony deck"></div></div>
  <p class="sold" style="left:429px; top:229px;"><strong>SOLD:</strong><br>$490k</p>

  <div class="listing-photo" style="left:527px; top:194px;"><div class="fill photo-lot" role="img" aria-label="Vacant lakeshore lot with marsh grass and open water"></div></div>
  <p class="tag" style="left:671px; top:222px;">N. Fern<br>Rd:<br><span class="status">Pending</span></p>

  <div class="listing-photo mystery" style="left:779px; top:195px;"><span>?</span></div>
  <p class="tag" style="left:928px; top:204px; line-height:31px;">Your Next<br>Lakeside<br>Property:<br><span class="status">???</span></p>

  <div class="brand-mark">
    <div class="dot"></div>
    <span class="name">Pinecove.net</span>
  </div>

  <div class="address-box"></div>

  <div class="announcement">
    <p class="title">New Office Opening in Shell Lake!</p>
    <p>Our new Shell Lake, WI office opens Spring 2016.</p>
    <p class="feature">As featured on RVMN's “Harborview Treasure Quest”</p>
  </div>

  <div class="agent-photo" role="img" aria-label="Agent headshot"></div>
  <p class="agent-name">Tom Harwell, Realtor/Associate Broker</p>
  <p class="agent-phone">555-302-8847</p>
</body>
</html>
```